Design some Business Cards

I need a business card designed front and back. The information I want on the card is below. I put the descriptions like name, title, etc but you don't need to include those. I like blue and an easy to read font and biggish font size.

Name: Dr. Marsha Tellman
Degrees: Ph.D., MSM
Title: Owner
Main company line: 866-CALL-SCRIBE
Office phone: (555) 803-6147
Cell phone: (555) 462-8035
Address: 2756 Maple Crest Ave.
Suite 14
Wellington, FL 33587
Website: http;//[url removed, login to view]
Email: marsha@[url removed, login to view]
Company tag line: Expert Words, Made Clear For All Readers.
Certifications: 8(a), EDWOSB, MOSB, SDB
CAGE code: 3KPR8
Primary NAICS code: 541990
Specialty: Medical, scientific and health writing/editing

I've attached some old cards that you can get the logo and RGB color of the blue I love, plus a flyer we use that has information on the company.

I need these asap so I will choose the first one that looks great. I will need the psd and the jpg files. Thanks!

```html
<!DOCTYPE html>
<html lang="en">
<head>
<meta charset="utf-8">
<title>ClearScribe Business Cards</title>
<link rel="stylesheet" href="https://fonts.googleapis.com/css2?family=Roboto:wght@400;500;700&display=swap">
<style>
  :root {
    --bg: #d9dadc;
    --blue-deep: #1d8ad3;
    --blue-light: #52c4ef;
    --blue-brand: #2a86c9;
    --white: #ffffff;
    --ink: #3a4048;
    --paper: #f4f5f6;
  }
  * { box-sizing: border-box; margin: 0; padding: 0; }
  html, body { width: 1200px; height: 900px; overflow: hidden; }
  body {
    background: var(--bg);
    font-family: "Roboto", Arial, sans-serif;
    position: relative;
  }
  .card {
    position: absolute;
    width: 640px;
    height: 366px;
    border-radius: 30px;
    overflow: hidden;
  }

  /* Front card */
  .card-front {
    left: 180px;
    top: 56px;
    background: linear-gradient(135deg, var(--blue-deep) 0%, var(--blue-light) 100%);
    color: var(--white);
  }
  .front-brand {
    position: absolute;
    left: 110px;
    top: 96px;
    display: flex;
    align-items: center;
    gap: 18px;
  }
  .brand-dot {
    width: 44px; height: 44px;
    border-radius: 50%;
    background: rgba(255,255,255,0.85);
    flex: none;
  }
  .front-brand .brand-name {
    font-size: 50px;
    font-weight: 500;
    letter-spacing: -0.5px;
    line-height: 1;
  }
  .front-brand .brand-tagline {
    font-size: 11.5px;
    font-weight: 500;
    letter-spacing: 0.6px;
    text-transform: uppercase;
    margin-top: 6px;
  }
  .front-details {
    position: absolute;
    left: 0; right: 0;
    top: 226px;
    text-align: center;
    font-size: 17px;
    line-height: 1.6;
  }

  /* Back card */
  .card-back {
    left: 380px;
    top: 478px;
    background: var(--paper);
  }
  .back-brand {
    position: absolute;
    left: 26px;
    top: 170px;
    width: 226px;
    display: flex;
    align-items: center;
    gap: 10px;
    color: var(--blue-brand);
  }
  .back-brand .brand-dot {
    width: 26px; height: 26px;
    background: var(--blue-brand);
  }
  .back-brand .brand-name {
    font-size: 33px;
    font-weight: 700;
    line-height: 1;
    letter-spacing: -0.5px;
    white-space: nowrap;
  }
  .back-brand .brand-tagline {
    font-size: 9.5px;
    font-weight: 500;
    color: var(--ink);
    margin-top: 5px;
    white-space: nowrap;
  }
  .info-panel {
    position: absolute;
    left: 262px;
    top: 0;
    width: 378px;
    height: 100%;
    background: linear-gradient(160deg, var(--blue-deep) 0%, var(--blue-light) 100%);
    clip-path: polygon(20px 0, 100% 0, 100% 100%, 20px 100%, 20px 78px, 0 62px, 20px 46px);
    color: var(--white);
    padding: 26px 20px 0 44px;
  }
  .person-name {
    font-size: 30px;
    font-weight: 700;
    line-height: 1.1;
  }
  .person-role {
    font-size: 13px;
    margin-top: 4px;
  }
  .address {
    font-size: 13.5px;
    line-height: 1.4;
    margin-top: 14px;
  }
  .contact-list {
    list-style: none;
    margin-top: 12px;
  }
  .contact-list li {
    display: flex;
    align-items: center;
    gap: 10px;
    font-size: 14px;
    height: 25px;
  }
  .contact-icon {
    width: 20px; height: 20px;
    border-radius: 50%;
    background: var(--white);
    display: flex;
    align-items: center;
    justify-content: center;
    flex: none;
  }
  .contact-icon svg { width: 12px; height: 12px; }
  .certifications {
    font-size: 13px;
    line-height: 1.35;
    margin-top: 12px;
  }
  .certifications strong { font-weight: 500; }
</style>
</head>
<body>

  <section class="card card-front">
    <div class="front-brand">
      <div class="brand-dot"></div>
      <div>
        <div class="brand-name">ClearScribe</div>
        <div class="brand-tagline">Expert words, made clear for all readers.</div>
      </div>
    </div>
    <div class="front-details">
      <p>Main company line: 866-CALL-SCRIBE</p>
      <p>Specialty: Medical, scientific and health writing/editing</p>
    </div>
  </section>

  <section class="card card-back">
    <div class="back-brand">
      <div class="brand-dot"></div>
      <div>
        <div class="brand-name">ClearScribe</div>
        <div class="brand-tagline">Expert Words, Made Clear For All Readers.</div>
      </div>
    </div>

    <div class="info-panel">
      <h1 class="person-name">Dr. Marsha Tellman</h1>
      <p class="person-role">Ph.D., MSM &nbsp;|&nbsp; Owner</p>
      <p class="address">2756 Maple Crest Ave. Suite 14<br>Wellington, FL 33587</p>

      <ul class="contact-list">
        <li>
          <span class="contact-icon">
            <svg viewBox="0 0 24 24"><path fill="#2a86c9" d="M6.6 10.8a15.1 15.1 0 0 0 6.6 6.6l2.2-2.2a1 1 0 0 1 1-.25 11.4 11.4 0 0 0 3.6.57 1 1 0 0 1 1 1V20a1 1 0 0 1-1 1A17 17 0 0 1 3 4a1 1 0 0 1 1-1h3.5a1 1 0 0 1 1 1c0 1.250.2 2.45.57 3.57a1 1 0 0 1-.25 1z"/></svg>
          </span>
          (555) 803-6147 (Office)
        </li>
        <li>
          <span class="contact-icon">
            <svg viewBox="0 0 24 24"><rect x="6" y="2" width="12" height="20" rx="2" fill="#2a86c9"/><rect x="8" y="5" width="8" height="12" fill="#fff"/></svg>
          </span>
          (555) 462-8035 (Cell)
        </li>
        <li>
          <span class="contact-icon">
            <svg viewBox="0 0 24 24"><rect x="2" y="5" width="20" height="14" rx="2" fill="#2a86c9"/><path d="M3 6l9 7 9-7" fill="none" stroke="#fff" stroke-width="2"/></svg>
          </span>
          marsha@clearscribewriters.com
        </li>
        <li>
          <span class="contact-icon">
            <svg viewBox="0 0 24 24"><circle cx="12" cy="12" r="9" fill="none" stroke="#2a86c9" stroke-width="2.4"/><path d="M3 12h18M12 3c3 3 3 15 0 18M12 3c-3 3-3 15 0 18" fill="none" stroke="#2a86c9" stroke-width="1.8"/></svg>
          </span>
          www.clearscribewriters.com
        </li>
      </ul>

      <div class="certifications">
        <p>Certifications:</p>
        <p>8(a), EDWOSB, MOSB, SDB</p>
        <p><strong>CAGE code: 3KPR8</strong></p>
        <p><strong>Primary NAICS code: 541990</strong></p>
      </div>
    </div>
  </section>

</body>
</html>
```